LumaVerge New Website

LumaVerge is a digital marketing agency. Our clients are all limousine companies. We need a responsive website designed to highlight our services and products. Our competition is http://www.clearpathgrowthhub.example/ and we need a site of similar design and layout without being too similar. Our old website www.lumaverge.example, is very outdated and the logo and graphics have changed. We will adjust the content to work with the new design. The new logo is attached.

```html
<!DOCTYPE html>
<html lang="en">
<head>
<meta charset="utf-8">
<title>LumaVerge — Marketing for Limousine Companies</title>
<link rel="stylesheet" href="https://fonts.googleapis.com/css2?family=Roboto:wght@400;500;700&family=Open+Sans:wght@400;600&display=swap">
<style>
:root{
  --navy:#1f4e7e;
  --button:#15325a;
  --lime:#a3bf1c;
  --ink:#222;
  --muted:#555;
  --soft:#ececec;
  --white:#fff;
  --footer:#2b2b2b;
  --footer-text:#d4d4d4;
  --social:#4a7ab5;
}
*{box-sizing:border-box;margin:0;padding:0}
html,body{width:1200px;height:2362px;overflow:hidden;background:var(--white)}
body{position:relative;font-family:"Open Sans",Arial,sans-serif;color:var(--ink)}
a{color:inherit;text-decoration:none}

/* header */
.site-header{position:absolute;left:0;top:0;width:1200px;height:80px;background:var(--white)}
.brand{position:absolute;left:165px;top:18px;font-family:"Roboto",Arial,sans-serif;font-weight:500;font-size:32px;line-height:40px;color:var(--navy)}
.contact-bar{position:absolute;right:165px;top:16px;font-family:"Roboto",Arial,sans-serif;font-size:13px;font-weight:500;display:flex;gap:18px;align-items:center}
.contact-bar span{display:flex;align-items:center;gap:6px}
.contact-bar .dot{width:13px;height:13px;border-radius:50%;background:var(--lime)}
.contact-bar .phone{color:var(--lime);font-weight:700}
.main-nav{position:absolute;right:165px;top:44px;display:flex;gap:20px;font-family:"Roboto",Arial,sans-serif;font-size:14px;font-weight:500;color:var(--ink)}

/* hero */
.hero{position:absolute;left:0;top:80px;width:1200px;height:470px;background:linear-gradient(180deg,#9fb2c4 0%,#c9d0d6 30%,#8d8f90 55%,#6f7071 100%)}
.hero-photo{position:absolute;inset:0}
.hero-title{position:absolute;left:165px;top:110px}
.hero-title span{display:inline-block;background:rgba(30,30,30,.8);color:var(--white);font-family:"Roboto",Arial,sans-serif;font-weight:500;font-size:38px;line-height:56px;padding:0 12px;margin-bottom:14px}
.btn{display:inline-block;background:var(--button);color:var(--white);font-family:"Roboto",Arial,sans-serif;font-weight:500;font-size:17px;border-radius:26px;text-align:center}
.hero .btn{position:absolute;left:165px;top:253px;width:284px;height:52px;line-height:52px}

/* features */
.features{position:absolute;left:0;top:550px;width:1200px;height:383px;background:var(--soft)}
.feature{position:absolute;top:60px;width:295px;text-align:center}
.feature-icon{display:block;margin:0 auto;height:62px}
.feature h3{font-family:"Roboto",Arial,sans-serif;font-weight:700;font-size:18px;margin-top:28px}
.feature p{font-size:12.5px;line-height:17px;color:var(--ink);margin-top:8px;height:96px}
.feature .more{font-size:13px;text-decoration:underline;color:var(--ink)}
.connector{position:absolute;left:597px;top:304px}

/* experience */
.experience{position:absolute;left:0;top:933px;width:1200px;height:380px;background:var(--navy);text-align:center;color:var(--white)}
.experience h2{font-family:"Roboto",Arial,sans-serif;font-weight:500;font-size:28px;margin-top:48px}
.experience p{width:800px;margin:22px auto 0;font-size:16px;line-height:25px}
.experience .highlight{color:var(--lime)}
.experience .btn{position:absolute;left:465px;top:257px;width:279px;height:52px;line-height:52px}

/* blog */
.blog{position:absolute;left:0;top:1313px;width:1200px;height:683px;background:var(--soft)}
.blog h2{text-align:center;font-family:"Roboto",Arial,sans-serif;font-weight:500;font-size:28px;margin-top:56px}
.post{position:absolute;top:144px;height:447px;overflow:hidden;background:var(--white);border-left:8px solid var(--lime);padding:24px 22px 0 23px}
.post-image{display:block;width:100%;height:149px}
.post h3{font-family:"Roboto",Arial,sans-serif;font-weight:400;font-size:24px;line-height:27px;margin-top:22px;color:var(--ink)}
.post p{font-size:12px;line-height:17px;color:var(--muted);margin-top:10px}

/* footer */
.site-footer{position:absolute;left:0;top:1996px;width:1200px;height:319px;background:var(--footer);color:var(--footer-text)}
.footer-col{position:absolute;top:46px;width:210px;font-size:12.5px;line-height:18px}
.footer-col h4{font-family:"Roboto",Arial,sans-serif;font-weight:700;font-size:14px;color:var(--white);margin-bottom:16px}
.footer-col .current{color:var(--lime)}
.social-row{display:flex;gap:5px;margin-bottom:6px}
.social-row i{display:block;width:16px;height:16px;background:var(--social)}
.copyright{position:absolute;left:0;top:2315px;width:1200px;height:47px;text-align:center;font-size:12px;line-height:47px;color:var(--muted)}
.copyright strong{color:var(--ink)}
</style>
</head>
<body>

<header class="site-header">
  <div class="brand">LumaVerge</div>
  <div class="contact-bar">
    <span><i class="dot"></i>E-mail: info@lumaverge.example</span>
    <span><i class="dot"></i>Toll Free: <b class="phone">555-014-2280</b></span>
  </div>
  <nav class="main-nav">
    <a href="#">Integrated Marketing</a>
    <a href="#">Services</a>
    <a href="#">News &amp; Events</a>
    <a href="#">LoyalLoop™</a>
    <a href="#">Blog</a>
    <a href="#">Contact Us</a>
  </nav>
</header>

<section class="hero">
  <div class="hero-photo" role="img" aria-label="White stretch limousine parked on a lot under a blue sky"></div>
  <h1 class="hero-title">
    <span>We Have A Passion For What We Do.</span><br>
    <span>Let Us Do What We Do Best ...</span>
  </h1>
  <a class="btn" href="#">Find more out about this.</a>
</section>

<section class="features">
  <div class="feature" style="left:155px">
    <svg class="feature-icon" width="62" height="62" viewBox="0 0 62 62" aria-hidden="true">
      <circle cx="31" cy="31" r="29" fill="var(--lime)"/>
      <circle cx="33" cy="17" r="4.5" fill="#fff"/>
      <path d="M27 26h10l-4 22h4l-1 4H25l1-4h3l3-18h-6z" fill="#fff"/>
    </svg>
    <h3>Changing the Game</h3>
    <p>We create opportunities for people to get excited about your company, which drives the creation of transactional value for your business. We create Fans - not just social fans - but people who pay attention to you and spend more money with you.</p>
    <a class="more" href="#">Read more</a>
  </div>
  <div class="feature" style="left:458px">
    <div class="feature-icon" role="img" aria-label="Limousine line icon" style="width:140px;height:52px;margin-top:10px;border:4px solid var(--navy);border-radius:10px 18px 8px 8px"></div>
    <h3>Limousine Industry Specialists</h3>
    <p>LumaVerge is All About Driving Results. Too many limousine and chauffeured ground transportation companies define their niche markets relative to what they think their customers are thinking, not what their target customer actually thinks.</p>
    <a class="more" href="#">Read more</a>
  </div>
  <div class="feature" style="left:760px">
    <div class="feature-icon" role="img" aria-label="Speaker with speech bubble icon" style="width:60px;background:var(--lime);border-radius:8px"></div>
    <h3>Your Marketing Message Matters</h3>
    <p>Being different is only the first step in attracting new business and retaining your current customers. But, just being different won't necessarily distance you from your competition. If you really want to be successful you have to be.</p>
    <a class="more" href="#">Read more</a>
  </div>
  <svg class="connector" width="16" height="79" viewBox="0 0 16 79" aria-hidden="true">
    <line x1="8" y1="0" x2="8" y2="6" stroke="var(--lime)" stroke-width="2"/>
    <circle cx="8" cy="13" r="7" fill="none" stroke="var(--lime)" stroke-width="2"/>
    <line x1="8" y1="20" x2="8" y2="79" stroke="var(--lime)" stroke-width="2"/>
  </svg>
</section>

<section class="experience">
  <h2>You're In the Experience Business.</h2>
  <p><span class="highlight">Like Meridian Coach, our top limousine</span> and corporate ground transportation clients are industry pioneers and success stories. They are the companies that are changing the chauffeured transportation experience. LumaVerge's clients provide quality service, make the best use of their resources and are authentic in their messaging. Their customers are excited about their companies, their people and their services. Sometimes, they'll even pay them a little bit more.</p>
  <a class="btn" href="#">Read more about this.</a>
</section>

<section class="blog">
  <h2>Latest from the blog.</h2>
  <article class="post" style="left:158px;width:279px">
    <div class="post-image" role="img" aria-label="Teddy bear buckled into a car seat" style="background:linear-gradient(135deg,#3a3a3a,#1c1c1c)"></div>
    <h3>The Strategic Choices we make.</h3>
    <p>I want to first thank the President of the Coastal Aviation Guild, Commodore Ray Hollis, for affording me this opportunity to join you for this important conference. I also want to commend this organization for 148 years of remarkable leadership, service, and advocacy on behalf of the aerospace community.</p>
  </article>
  <article class="post" style="left:465px;width:279px">
    <div class="post-image" role="img" aria-label="Businessman marking a review rating on a glass screen" style="background:linear-gradient(135deg,#e6ebe9,#b9c3c6)"></div>
    <h3>How to Avoid Bad Online Reviews.</h3>
    <p>I want to first thank the President of the Coastal Aviation Guild, Commodore Ray Hollis, for affording me this opportunity to join you for this important conference. I also want to commend this organization for 148 years of remarkable leadership, service, and advocacy on behalf of the aerospace community.</p>
  </article>
  <article class="post" style="left:770px;width:272px">
    <div class="post-image" role="img" aria-label="Network of connected social media bubbles" style="background:linear-gradient(135deg,#4f6c80,#2f4656)"></div>
    <h3>Social Media Tips and Tricks.</h3>
    <p>I want to first thank the President of the Coastal Aviation Guild, Commodore Ray Hollis, for affording me this opportunity to join you for this important conference. I also want to commend this organization for 148 years of remarkable leadership, service, and advocacy on behalf of the aerospace community.</p>
  </article>
</section>

<footer class="site-footer">
  <div class="footer-col" style="left:165px">
    <h4>LumaVerge.</h4>
    <div>Home</div>
    <div class="current">Online Image &amp; Reputation</div>
    <div>Management</div>
    <div>Blog</div>
  </div>
  <div class="footer-col" style="left:390px">
    <h4>Customerservice.</h4>
    <div>Contact</div>
    <div>FAQ</div>
    <div>Customer Retention &amp; Loyalty</div>
    <div>Mobile Marketing</div>
    <div>OutBound Marketing</div>
  </div>
  <div class="footer-col" style="left:616px;width:200px">
    <h4>Socialmedia.</h4>
    <div class="social-row"><i></i><i></i><i></i><i></i></div>
    <div>Morbi blandit sagittis tortor, quis cursus diam. Aenean nec velit volutpat, pharetra mi vestibulum, faucibus massa. Integer suscipit sollicitudin justo non gravida.</div>
  </div>
  <div class="footer-col" style="left:841px">
    <h4>Others.</h4>
    <div>Terms and conditions</div>
    <div>Support to Complete the Sale</div>
    <div>Social Media Marketing</div>
    <div>Inbound Marketing</div>
  </div>
</footer>
<div class="copyright">© 2013 - 2014 <strong>LumaVerge.example</strong>. All rights reserved</div>

</body>
</html>
```